Web application layout remake

We are looking for a makeover on our web application called “QVLcrate” - it's a document management and digital archiving system integrating workflows and allowing you to free up physical space in your office currently occupied with documents by moving them to secure external custody.
We are expecting you to include the following:
• homepage
• signup page
• application page
This project is for the whole website (which is not big at all anyway!) and not just for the design of one page. The coding should be in HTML5 only.
We are aiming for fresh, appealing, clean, user friendly ,web 2.0, jquery layout.
Remakes or changes on the logo are welcome.
The application will be sold through the portal.
Please find in attachment the print screen of the application to aid you (this is the current view customers have after logging in but the layout is obsolete and we want a brand new!).
Reason: Still not happy with the received layouts. Keep up the good work! Thanks!
Reason: Still not happy with the whole solution and finding alternate app interfaces!
Industry/Entity Type
Digital
Look and feel
Each slider illustrates characteristics of the customer's brand and the style your logo design should communicate.

```html
<!DOCTYPE html>
<html lang="pt">
<head>
<meta charset="utf-8">
<title>QVLcrate – Actas</title>
<link rel="stylesheet" href="https://fonts.googleapis.com/css2?family=Noto+Sans:wght@400;700&family=Lato:wght@400;700&display=swap">
<style>
:root{
  --blue:#0a5fd6;--blue-dark:#0448b0;--blue-light:#5aa5f5;
  --side:#2b313b;--side-line:#1c2027;--side-head:#242931;
  --content:#eaf6fd;--bar:#dfe3e8;--ink:#333;--muted:#555;
  --white:#fff;--footer:#2d3138;
}
*{box-sizing:border-box;margin:0;padding:0}
html,body{width:1200px;height:750px;overflow:hidden}
body{position:relative;font-family:"Noto Sans",sans-serif;background:var(--content);color:var(--ink);font-size:12px}
.abs{position:absolute}
.topbar{left:0;top:0;width:1200px;height:50px;background:linear-gradient(#1a72e8,#0750c2)}
.brand{left:23px;top:15px;color:var(--white);font-size:19px;letter-spacing:-.5px}
.navbtn{top:12px;height:25px;border:1px solid #042f78;border-radius:3px;background:linear-gradient(#1664d8,#0747b0);color:var(--white);font-weight:700;font-size:12.5px;display:flex;align-items:center;justify-content:center;gap:6px}
.chev{width:13px;height:13px}
.logout{left:990px;top:17px;color:var(--white);font-weight:700;font-size:12.5px}
.search{left:1022px;top:13px;width:153px;height:24px;border-radius:12px;background:var(--white);border:1px solid #9bb;padding:3px 12px;font-size:12px;color:#333}
.search svg{position:absolute;right:9px;top:5px}
.stripe{left:0;top:50px;width:1200px;height:17px;background:repeating-linear-gradient(45deg,#2e2e2e 0 2px,#3a3a3a 2px 4px)}
.sidebar{left:0;top:67px;width:250px;height:658px;background:var(--side)}
.sidehead{left:0;width:250px;height:25px;background:var(--side-head);border-bottom:1px solid var(--side-line);color:var(--white);font-weight:700;font-size:12px;padding:5px 13px}
.tree{font-family:"Lato",sans-serif;color:var(--white);font-size:10.5px}
.sep{left:0;width:250px;height:1px;background:var(--side-line)}
.toggle{left:227px;width:13px;height:13px}
.empty{left:13px;top:380px;color:#4b525d;font-size:9.5px;font-family:"Lato",sans-serif}
.crumbbar{left:250px;top:67px;width:950px;height:33px;background:linear-gradient(#c6cbd1,#a9b0b8);color:#444;font-size:12px;padding:8px 50px}
.crumbbar svg{position:absolute;left:16px;top:7px}
.bar{left:250px;width:950px;height:25px;background:linear-gradient(#f6f7f8,#d7dbe0);border-top:1px solid #bbb;border-bottom:1px solid #bbb;padding:4px 15px;font-size:12px;color:#444}
.label{left:271px;font-size:12px}
.sel{height:18px;border:1px solid #555;border-radius:2px;background:linear-gradient(#fff,#ddd);font-size:11.5px;padding:0 8px;line-height:16px}
.sel svg{position:absolute;right:5px;top:3px}
.inp{left:574px;width:234px;height:18px;border:1px solid #333;border-radius:2px;background:var(--white);font-size:12px;padding:0 8px;line-height:16px}
.btn{top:283px;width:83px;height:25px;border-radius:2px;color:var(--white);font-weight:700;font-size:12px;display:flex;align-items:center;justify-content:center}
.btn.primary{left:450px;background:linear-gradient(#1a6ee3,#0546ae);border:1px solid #03337f}
.btn.dark{left:550px;background:linear-gradient(#444,#1b1b1b);border:1px solid #000}
.pager{left:266px;width:917px;height:19px;font-size:12px}
.pager .sel{position:absolute;left:0;top:0;width:142px}
.pager .nav{position:absolute;left:427px;top:1px;display:flex;align-items:center;gap:4px}
.pager .lbl{position:absolute;left:776px;top:1px}
.pager .num{position:absolute;left:833px;top:0;width:43px;height:18px;border:1px solid #333;background:#fff;border-radius:2px}
.pager .go{position:absolute;left:884px;top:1px;width:33px;height:16px;background:linear-gradient(#444,#111);color:#fff;font-weight:700;font-size:11px;text-align:center;line-height:16px;border-radius:2px}
table{position:absolute;left:267px;top:417px;width:916px;border-collapse:collapse;background:var(--white)}
th{background:linear-gradient(#1670e6,#0654c8);color:var(--white);font-size:13.5px;height:32px;border:1px solid #0340a0}
td{height:42px;border:1px solid #444;text-align:center;color:#666;font-size:12px}
.acts{display:flex;gap:13px;justify-content:center}
.menu{left:714px;top:42px;width:166px;background:#f3f3f3;border:1px solid #999;box-shadow:0 2px 4px rgba(0,0,0,.3);font-family:"Lato",sans-serif;font-size:10.5px;color:#111}
.menu div{height:25px;padding:6px 8px;border-bottom:1px solid #ccc;position:relative}
.menu .on{background:var(--blue-light);color:#0a2a66}
.menu .on svg{position:absolute;right:8px;top:5px}
.sub{left:875px;top:96px;width:100px}
.footer{left:0;top:725px;width:1200px;height:25px;background:var(--footer);color:#999;font-size:10px;text-align:center;line-height:25px;font-family:"Lato",sans-serif}
</style>
</head>
<body>
<header class="abs topbar"></header>
<div class="abs brand">QVLcrate</div>
<div class="abs navbtn" style="left:691px;width:57px">Inicio</div>
<div class="abs navbtn" style="left:762px;width:70px">Menu <svg class="chev" viewBox="0 0 14 14"><circle cx="7" cy="7" r="6.5" fill="#fff"/><path d="M4 5.5l3 3 3-3" stroke="#0750c2" stroke-width="1.8" fill="none"/></svg></div>
<div class="abs navbtn" style="left:845px;width:125px">Administracao <svg class="chev" viewBox="0 0 14 14"><circle cx="7" cy="7" r="6.5" fill="#fff"/><path d="M4 5.5l3 3 3-3" stroke="#0750c2" stroke-width="1.8" fill="none"/></svg></div>
<div class="abs logout">Sair</div>
<div class="abs search">Pesquisar<svg width="14" height="14" viewBox="0 0 14 14"><circle cx="5.5" cy="5.5" r="4.2" stroke="#222" stroke-width="2" fill="none"/><path d="M8.6 8.6l4 4" stroke="#222" stroke-width="2.4"/></svg></div>
<div class="abs stripe"></div>

<aside class="abs sidebar"></aside>
<div class="abs sidehead" style="top:67px">Explorador</div>
<svg class="abs" style="left:16px;top:102px" width="27" height="20" viewBox="0 0 27 20"><path d="M1 3h8l2 2h12v3H5L1 18z" fill="#ddd"/><path d="M5 8h21l-4 11H1z" fill="#fff"/></svg>
<div class="abs tree" style="left:50px;top:105px">ADMINISTRACAO</div>
<svg class="abs toggle" style="top:105px" viewBox="0 0 14 14"><circle cx="7" cy="7" r="6.5" fill="#ccc"/><path d="M3.5 7h7" stroke="#333" stroke-width="2"/></svg>
<svg class="abs" style="left:49px;top:132px" width="27" height="20" viewBox="0 0 27 20"><path d="M1 3h8l2 2h12v3H5L1 18z" fill="#ddd"/><path d="M5 8h21l-4 11H1z" fill="#fff"/></svg>
<div class="abs tree" style="left:84px;top:135px">Actas</div>
<svg class="abs" style="left:49px;top:165px" width="27" height="20" viewBox="0 0 27 20"><path d="M1 3h8l2 2h12v3H5L1 18z" fill="#ddd"/><path d="M5 8h21l-4 11H1z" fill="#fff"/></svg>
<div class="abs tree" style="left:84px;top:168px">Geral</div>
<svg class="abs" style="left:49px;top:198px" width="27" height="20" viewBox="0 0 27 20"><path d="M1 3h8l2 2h12v3H5L1 18z" fill="#ddd"/><path d="M5 8h21l-4 11H1z" fill="#fff"/></svg>
<div class="abs tree" style="left:84px;top:201px">Secretariado</div>
<div class="abs sep" style="top:228px"></div>
<svg class="abs" style="left:16px;top:240px" width="23" height="18" viewBox="0 0 23 18"><path d="M0 2h8l2 2h13v14H0z" fill="#fff"/></svg>
<div class="abs tree" style="left:50px;top:242px">CLIENTES</div>
<svg class="abs toggle" style="top:243px" viewBox="0 0 14 14"><circle cx="7" cy="7" r="6.5" fill="#ccc"/><path d="M3.5 7h7M7 3.5v7" stroke="#333" stroke-width="2"/></svg>
<div class="abs sep" style="top:266px"></div>
<svg class="abs" style="left:16px;top:278px" width="23" height="18" viewBox="0 0 23 18"><path d="M0 2h8l2 2h13v14H0z" fill="#fff"/></svg>
<div class="abs tree" style="left:50px;top:280px">DEP. INFORMATICA</div>
<svg class="abs toggle" style="top:281px" viewBox="0 0 14 14"><circle cx="7" cy="7" r="6.5" fill="#ccc"/><path d="M3.5 7h7M7 3.5v7" stroke="#333" stroke-width="2"/></svg>
<div class="abs sep" style="top:304px"></div>
<svg class="abs" style="left:16px;top:315px" width="23" height="18" viewBox="0 0 23 18"><path d="M0 2h8l2 2h13v14H0z" fill="#fff"/></svg>
<div class="abs tree" style="left:50px;top:317px">RECLAMACOES</div>
<svg class="abs toggle" style="top:318px" viewBox="0 0 14 14"><circle cx="7" cy="7" r="6.5" fill="#ccc"/><path d="M3.5 7h7M7 3.5v7" stroke="#333" stroke-width="2"/></svg>
<div class="abs sidehead" style="top:342px;border-top:1px solid var(--side-line)">Alertas</div>
<div class="abs empty">Nao existem alertas.</div>

<div class="abs crumbbar"><svg width="26" height="18" viewBox="0 0 26 18"><path d="M1 2h8l2 2h12v3H5L1 17z" fill="#555"/><path d="M5 7h20l-4 10H1z" fill="#333"/></svg>ADMINISTRACAO / Actas</div>
<div class="abs bar" style="top:100px">Pesqulsa</div>

<div class="abs label" style="top:150px">#</div>
<div class="abs sel" style="left:449px;top:150px;width:109px">=<svg width="8" height="11" viewBox="0 0 8 11"><path d="M4 0l4 4H0zM4 11l4-4H0z" fill="#222"/></svg></div>
<div class="abs inp" style="top:150px">asdfafdsafafs</div>
<div class="abs label" style="top:183px">Tipo</div>
<div class="abs sel" style="left:449px;top:183px;width:218px">Choose one<svg width="8" height="11" viewBox="0 0 8 11"><path d="M4 0l4 4H0zM4 11l4-4H0z" fill="#222"/></svg></div>
<div class="abs label" style="top:216px">Data Entrada</div>
<div class="abs sel" style="left:449px;top:216px;width:109px">=<svg width="8" height="11" viewBox="0 0 8 11"><path d="M4 0l4 4H0zM4 11l4-4H0z" fill="#222"/></svg></div>
<div class="abs inp" style="top:216px">asdfafdsafafs</div>
<div class="abs label" style="top:250px">Comentario</div>
<div class="abs sel" style="left:449px;top:250px;width:109px">Contem<svg width="8" height="11" viewBox="0 0 8 11"><path d="M4 0l4 4H0zM4 11l4-4H0z" fill="#222"/></svg></div>
<div class="abs inp" style="top:250px">asdfafdsafafs</div>
<div class="abs btn primary">Search</div>
<div class="abs btn dark">Reset</div>

<div class="abs bar" style="top:333px">Pesqulsa Avancada</div>

<div class="abs pager" style="top:383px">
  <div class="sel">16 itens por pagina<svg width="8" height="11" viewBox="0 0 8 11"><path d="M4 0l4 4H0zM4 11l4-4H0z" fill="#222"/></svg></div>
  <div class="nav"><svg width="12" height="12" viewBox="0 0 12 12"><circle cx="6" cy="6" r="6" fill="#222"/><path d="M7.5 3L4 6l3.5 3z" fill="#fff"/></svg>1 of 1<svg width="12" height="12" viewBox="0 0 12 12"><circle cx="6" cy="6" r="6" fill="#222"/><path d="M4.5 3L8 6 4.5 9z" fill="#fff"/></svg></div>
  <div class="lbl">Pagina #</div><div class="num"></div><div class="go">ir!</div>
</div>

<table>
  <tr><th style="width:83px">#</th><th style="width:142px">Tipo</th><th style="width:208px">Data Entrada</th><th style="width:283px">Comentario</th><th style="width:75px">Caixa</th><th style="width:125px"></th></tr>
  <tr><td>1</td><td>Requirementos</td><td>2013-01-16</td><td></td><td></td>
  <td><div class="acts">
    <svg width="11" height="12" viewBox="0 0 11 12"><path d="M1 0h6l3 3v9H1z" fill="#222"/><path d="M3 9c2-1 3-3 3-6M3 9h5" stroke="#fff" stroke-width="1"/></svg>
    <svg width="12" height="12" viewBox="0 0 12 12"><path d="M1 11l1-3 7-7 2 2-7 7z" fill="#222"/></svg>
    <svg width="12" height="12" viewBox="0 0 12 12"><circle cx="6" cy="6" r="5.5" fill="#222"/><path d="M3 6h6" stroke="#fff" stroke-width="2"/></svg>
    <svg width="12" height="12" viewBox="0 0 12 12"><path d="M0 1h12v11H0z" fill="#222"/><path d="M1 4h10M1 7h10M1 10h10M3 2v10M6 2v10M9 2v10" stroke="#fff" stroke-width=".8"/></svg>
    <svg width="12" height="12" viewBox="0 0 12 12"><path d="M3 0h9v10H3z" fill="#222"/><path d="M1 2h8v10H1z" fill="#222" stroke="#fff" stroke-width=".8"/></svg>
  </div></td></tr>
</table>

<div class="abs pager" style="top:508px">
  <div class="sel">16 itens por pagina<svg width="8" height="11" viewBox="0 0 8 11"><path d="M4 0l4 4H0zM4 11l4-4H0z" fill="#222"/></svg></div>
  <div class="nav"><svg width="12" height="12" viewBox="0 0 12 12"><circle cx="6" cy="6" r="6" fill="#222"/><path d="M7.5 3L4 6l3.5 3z" fill="#fff"/></svg>1 of 1<svg width="12" height="12" viewBox="0 0 12 12"><circle cx="6" cy="6" r="6" fill="#222"/><path d="M4.5 3L8 6 4.5 9z" fill="#fff"/></svg></div>
  <div class="lbl">Pagina #</div><div class="num"></div><div class="go">ir!</div>
</div>

<nav class="abs menu">
  <div>Adicionar Documento</div>
  <div>Ver Documentos WorkFlow</div>
  <div class="on" style="border-bottom:0">Ver Alertas<svg width="15" height="15" viewBox="0 0 15 15"><circle cx="7.5" cy="7.5" r="7" fill="#333" stroke="#eee"/><path d="M6 4.5l3 3-3 3" stroke="#fff" stroke-width="1.6" fill="none"/></svg></div>
</nav>
<nav class="abs menu sub">
  <div>Alertas Abertos</div>
  <div class="on">Alertas Fechados</div>
  <div style="border-bottom:0">Alertas Atraso</div>
</nav>

<footer class="abs footer">Copyright 2013 QVLcrate</footer>
</body>
</html>
```